Real Estate Business Card Design

My name is Lorraine Whitcombe, I am a real estate agent with Harrowgate Realty and I'm currently looking for some designs for a new business card. I just recently had new headshots done and would love something creative, a fresh new look. Here are a few ideas I had in mind for my business cards and logos etc. that should be incorporated. The colors can be changed and if you look on my real estate website there is a plum color I would like to incorporate www.ellisvanehomesnx.com

There you will also find my information I would like included on my business cards.

Thank you!

Let me know if you have any questions.

Target Market(s)

Real Estate

Industry/Entity Type

Real Estate Agent

Contact Information for Business Card

Harrowgate Realty
Lorraine Whitcombe
482 Tarrow Lane
N. Brindle MA 02918
lorraine@ellisvanehomesnx.com
Cell: 508-317-6092
Office: 508-794-0381

Font styles to use
Serif
Sans Serif
Script

Requirements
Must have
• Clean and Modern Design with something that makes it stand out apart from the rest of generic real estate business cards. Clear and Easy to read. Professional look

```html
<!DOCTYPE html>
<html lang="en">
<head>
<meta charset="utf-8">
<title>Lorraine Whitcombe — Business Card</title>
<link href="https://fonts.googleapis.com/css2?family=Cormorant+Garamond:wght@500;600&family=Great+Vibes&family=Open+Sans:wght@400;600&display=swap" rel="stylesheet">
<style>
  :root {
    --canvas: #e9e6e1;
    --card-dark: #050505;
    --card-mid: #1c1c1c;
    --gold: #d9b25a;
    --ink-light: #f4f1ea;
    --ink-muted: #d8d4cc;
    --brand-blue: #5f9ad6;
  }
  * { margin: 0; padding: 0; box-sizing: border-box; }
  html, body { width: 1200px; height: 996px; overflow: hidden; }
  body { background: var(--canvas); position: relative; }

  .card {
    position: absolute;
    left: 250px;
    width: 700px;
    height: 400px;
    background: linear-gradient(135deg, var(--card-dark) 0%, var(--card-mid) 55%, var(--card-dark) 100%);
    box-shadow: 0 10px 30px rgba(0,0,0,.25);
    overflow: hidden;
  }
  .card--front { top: 78px; }
  .card--back { top: 518px; }

  .card__frame { position: absolute; inset: 0; width: 700px; height: 400px; }

  /* Front */
  .front__mark {
    position: absolute; left: 50%; top: 112px;
    width: 54px; height: 54px; margin-left: -27px;
    border-radius: 50%; background: var(--gold);
  }
  .front__name {
    position: absolute; left: 0; right: 0; top: 186px;
    text-align: center;
    font-family: "Cormorant Garamond", serif;
    font-weight: 600; font-size: 40px; letter-spacing: 1px;
    color: var(--ink-light);
  }
  .front__title {
    position: absolute; left: 0; right: 0; top: 248px;
    text-align: center;
    font-family: "Open Sans", sans-serif;
    font-size: 14px; letter-spacing: 7px;
    color: var(--ink-muted);
  }

  /* Back */
  .back__photo {
    position: absolute; left: 100px; top: 140px;
    width: 260px; height: 260px;
    background: radial-gradient(ellipse at 50% 45%, #d7b98f 0%, #a88460 35%, #3a2a1e 70%, rgba(5,5,5,0) 100%);
  }
  .back__brand {
    position: absolute; right: 64px; top: 58px;
    font-family: "Open Sans", sans-serif;
    font-weight: 600; font-size: 16px;
    color: var(--brand-blue);
  }
  .back__info {
    position: absolute; left: 380px; top: 100px;
    width: 260px;
  }
  .back__name {
    font-family: "Great Vibes", cursive;
    font-weight: 400;
    font-size: 34px; line-height: 1.2;
    word-spacing: 8px;
    color: var(--gold);
    white-space: nowrap;
    margin-bottom: 14px;
  }
  .back__contacts {
    list-style: none;
    font-family: "Open Sans", sans-serif;
    font-size: 12px; color: var(--ink-light);
  }
  .back__contacts li {
    display: flex; align-items: center; gap: 9px;
    margin-bottom: 11px; white-space: nowrap;
  }
  .contact__icon { width: 15px; height: 15px; flex: none; }
</style>
</head>
<body>

  <section class="card card--front" aria-label="Card front">
    <svg class="card__frame" viewBox="0 0 700 400" aria-hidden="true">
      <g stroke="#d9b25a" stroke-width="1" fill="none">
        <line x1="25" y1="45" x2="675" y2="45"/>
        <line x1="25" y1="355" x2="675" y2="355"/>
        <line x1="45" y1="25" x2="45" y2="375"/>
        <line x1="655" y1="25" x2="655" y2="375"/>
      </g>
    </svg>
    <div class="front__mark" aria-hidden="true"></div>
    <h1 class="front__name">LORRAINE WHITCOMBE</h1>
    <p class="front__title">REALTOR®</p>
  </section>

  <section class="card card--back" aria-label="Card back">
    <div class="back__photo" role="img" aria-label="Headshot photograph of the agent"></div>
    <svg class="card__frame" viewBox="0 0 700 400" aria-hidden="true">
      <g stroke="#d9b25a" stroke-width="1" fill="none">
        <line x1="25" y1="45" x2="675" y2="45"/>
        <line x1="25" y1="355" x2="675" y2="355"/>
        <line x1="45" y1="25" x2="45" y2="375"/>
        <line x1="655" y1="25" x2="655" y2="375"/>
      </g>
    </svg>
    <p class="back__brand">Harrowgate Realty</p>
    <div class="back__info">
      <h2 class="back__name">Lorraine&nbsp; Whitcombe</h2>
      <ul class="back__contacts">
        <li>
          <svg class="contact__icon" viewBox="0 0 16 16" aria-hidden="true"><circle cx="8" cy="8" r="8" fill="#d9b25a"/><path d="M8 3.5a3 3 0 0 0-3 3c0 2.2 3 5.8 3 5.8s3-3.6 3-5.8a3 3 0 0 0-3-3zm0 4.2a1.2 1.2 0 1 1 0-2.4 1.2 1.2 0 0 1 0 2.4z" fill="#111"/></svg>
          <span>482 Tarrow Lane N. Brindle MA 02918</span>
        </li>
        <li>
          <svg class="contact__icon" viewBox="0 0 16 16" aria-hidden="true"><circle cx="8" cy="8" r="8" fill="#d9b25a"/><rect x="4" y="5" width="8" height="6" fill="none" stroke="#111" stroke-width="1.2"/><path d="M4 5l4 3.2L12 5" fill="none" stroke="#111" stroke-width="1.2"/></svg>
          <span>lorraine@ellisvanehomesnx.com</span>
        </li>
        <li>
          <svg class="contact__icon" viewBox="0 0 16 16" aria-hidden="true"><circle cx="8" cy="8" r="8" fill="#d9b25a"/><path d="M5.6 4.2l1.3 1.8-.8 1c.5 1 1.3 1.8 2.3 2.3l1-.8 1.8 1.3-.7 1.5c-2.8-.3-5.3-2.8-5.6-5.6z" fill="#111"/></svg>
          <span>(M) 508-317-6092 | (O) 508-794-0381</span>
        </li>
      </ul>
    </div>
  </section>

</body>
</html>
```